Face book & Instagram ad needed

I am in need of a simple static image ad to be used for Facebook & Instagram. A photo of a nice roof on a nice house. "Instant Satellite Roof Estimates" "Your house, your time & instant estimate" . Our logo file is here: https://www.filvorra.example/scl/fo/q37tmw5ze81kpdaxnrb0z/KTbWP9GMLnhVc4XeqsFTa2w?rlkey=zx7ve2kam4ndpt63bqyjr5w4c&dl=0

Multiple variations will be purchased.

```html
<!DOCTYPE html>
<html lang="en">
<head>
<meta charset="utf-8">
<title>Instant Satellite Roof Estimates – Hollowbrook Roofing</title>
<link rel="stylesheet" href="https://fonts.googleapis.com/css2?family=Fira+Sans:wght@500;600&family=Roboto:wght@700&display=swap">
<style>
  :root {
    --page-bg: #e9eef1;
    --panel-grey: #e6e6e6;
    --teal-deep: #2e7d97;
    --teal-light: #5aa3bb;
    --headline-white: #ffffff;
    --headline-yellow: #f3e15c;
    --brand-ink: #1a1a1a;
  }
  * { box-sizing: border-box; margin: 0; padding: 0; }
  html, body {
    width: 1200px;
    height: 1155px;
    overflow: hidden;
    background: var(--page-bg);
  }
  .ad {
    position: absolute;
    left: 92px;
    top: 69px;
    width: 1014px;
    height: 1016px;
    background: var(--panel-grey);
    overflow: hidden;
  }
  .ad-shapes {
    position: absolute;
    inset: 0;
    width: 100%;
    height: 100%;
  }
  .headline {
    position: absolute;
    left: 443px;
    top: 381px;
    font-family: "Fira Sans", sans-serif;
    font-weight: 600;
    font-size: 64px;
    line-height: 82px;
    letter-spacing: 1px;
    text-transform: uppercase;
    white-space: nowrap;
    color: var(--headline-white);
  }
  .headline .accent { color: var(--headline-yellow); display: block; }
  .tagline {
    position: absolute;
    left: 443px;
    top: 646px;
    font-family: "Roboto", sans-serif;
    font-weight: 700;
    font-size: 45px;
    line-height: 61px;
    white-space: nowrap;
    color: var(--headline-white);
  }
  .brand {
    position: absolute;
    left: 36px;
    top: 812px;
    font-family: "Fira Sans", sans-serif;
    font-weight: 500;
    font-size: 40px;
    line-height: 48px;
    letter-spacing: 1px;
    color: var(--brand-ink);
  }
  .brand span { display: block; }
</style>
</head>
<body>
  <main class="ad">
    <svg class="ad-shapes" viewBox="0 0 878 880" preserveAspectRatio="none">
      <defs>
        <linearGradient id="house-photo-tone" x1="0" y1="0" x2="0" y2="1">
          <stop offset="0" stop-color="#e9904a"/>
          <stop offset="0.12" stop-color="#c77a45"/>
          <stop offset="0.22" stop-color="#3c4a2a"/>
          <stop offset="0.35" stop-color="#3a4147"/>
          <stop offset="0.6" stop-color="#4a4f55"/>
          <stop offset="0.8" stop-color="#6b5a45"/>
          <stop offset="1" stop-color="#5e5246"/>
        </linearGradient>
        <linearGradient id="teal-overlay" x1="0" y1="0" x2="0" y2="1">
          <stop offset="0" stop-color="#2e7d97" stop-opacity="0.72"/>
          <stop offset="0.55" stop-color="#2e7d97" stop-opacity="0.9"/>
          <stop offset="1" stop-color="#5aa3bb"/>
        </linearGradient>
      </defs>
      <path class="house-photo" role="img"
            aria-label="Photo: stone house with dark standing-seam metal roof at sunset, trees behind"
            d="M0 0 H878 V880 H430 Q300 650 0 615 Z" fill="url(#house-photo-tone)"/>
      <path class="teal-sweep" d="M740 0 H878 V880 H440 C360 720 350 430 470 260 C560 130 650 50 740 0 Z"
            fill="url(#teal-overlay)"/>
    </svg>

    <h1 class="headline">Instant
      <span class="accent">Satellite</span>
      <span class="accent">Roof Estimates</span>
    </h1>
    <p class="tagline">Your House, Your Time<br>&amp; Instant Estimate.</p>

    <div class="brand"><span>Hollowbrook</span><span>Roofing</span></div>
  </main>
</body>
</html>
```